Software allocation system needs a business card design

We need a business card designed for our software platform - www.rostellio.com.au

At the moment the logo and website is all black and white, we are happy for suggestions on implementing some colour throughout either the logo or business card.

Industry/Entity Type

Software

Font styles to use
Sans Serif

Colors

Designer to choose colors to be used in the design.

```html
<!DOCTYPE html>
<html lang="en">
<head>
<meta charset="utf-8">
<title>Rostellio Business Card</title>
<link rel="stylesheet" href="https://fonts.googleapis.com/css2?family=Didact+Gothic&display=swap">
<style>
  :root {
    --page-bg: #e9ecee;
    --card-white: #ffffff;
    --band-deep: #1a87b3;
    --band-light: #8ccbd1;
    --brand-grey: #4a4f55;
    --accent-teal: #8fd0d3;
    --heading-teal: #14707a;
    --contact-white: #ffffff;
    --font-main: "Didact Gothic", "Century Gothic", sans-serif;
  }
  html, body {
    margin: 0;
    width: 1200px;
    height: 900px;
    overflow: hidden;
    background: var(--page-bg);
  }
  .canvas {
    position: relative;
    width: 1200px;
    height: 900px;
    display: flex;
    align-items: center;
    justify-content: center;
  }
  .card {
    position: relative;
    width: 1000px;
    height: 572px;
    background: var(--card-white);
    box-shadow: 0 6px 24px rgba(0,0,0,0.12);
    overflow: hidden;
    font-family: var(--font-main);
  }
  .card-shapes {
    position: absolute;
    inset: 0;
  }
  .brand {
    position: absolute;
    left: 80px;
    top: 90px;
  }
  .brand-name {
    margin: 0;
    font-size: 62px;
    font-weight: 400;
    letter-spacing: 6px;
    color: var(--brand-grey);
    line-height: 1;
  }
  .brand-tagline {
    margin: 14px 0 0 4px;
    font-size: 18px;
    letter-spacing: 2.5px;
    text-transform: uppercase;
    color: var(--accent-teal);
  }
  .contact {
    position: absolute;
    left: 380px;
    top: 390px;
    color: var(--contact-white);
  }
  .contact-heading {
    margin: 0 0 10px;
    font-size: 32px;
    font-weight: 400;
    color: var(--heading-teal);
  }
  .contact-line {
    margin: 0 0 0 36px;
    font-size: 24px;
    line-height: 1.35;
  }
</style>
</head>
<body>
  <main class="canvas">
    <article class="card">
      <svg class="card-shapes" width="1000" height="572" viewBox="0 0 1000 572">
        <polygon class="band-deep" role="img" aria-label="Band of deep blue triangle pattern" points="0,380 360,300 1000,150 1000,572 0,572" fill="var(--band-deep)"/>
        <polygon class="band-light" points="170,572 360,350 1000,210 1000,572" fill="var(--band-light)"/>
        <circle class="corner-dot" cx="840" cy="92" r="54" fill="var(--accent-teal)"/>
      </svg>

      <header class="brand">
        <h1 class="brand-name">ROSTELLIO</h1>
        <p class="brand-tagline">Planning &amp; Compliance for Heavy Industry</p>
      </header>

      <section class="contact">
        <h2 class="contact-heading">Contac Us</h2>
        <p class="contact-line">PO Box 712</p>
        <p class="contact-line">Ashwood NSW 2117</p>
        <p class="contact-line">hello@rostellio.com.au</p>
      </section>
    </article>
  </main>
</body>
</html>
```